MY BEST MARKETING TOOL 8 PAGE FULL COLOR BOOKLET TO PHYSICIANS

I HAVE CORRECT DATA IN RIGHT PLACES. NEED HELP WITH FINISHING TOUCHES TO MAKE IT LOOK PROFESSIONAL AND GET IT PRINT READY. I HAVE USED CANVA TO GET THIS FAR. SO IF I NEED TO SHARE CANVA WITH YOU, HAPPY TO DO SO. THESE BOOKLETS WILL BE USED IN MARKETING. AUDIENCE IS DOCTORS. I WANT INFO TO BE CLEAR AND EASY TO FOLLOW.
Updates

MY FAVORITE COLORS ARE NAVY BLUE, COLUMBIA (SKY BLUE), LIGHT GRAY, SILVER, AND WHITE. THINK THESE SHOULD BE BASIC COLOR RANGE.

TRY TO USE LARGER TEXT PLEASE.

WEBSITE FOR BUSINESS---------------BRAVELTON318.COM

Target Market(s)

FAMILY MEDICINE PHYSICIANS

Industry/Entity Type

MEDICAL

Font styles to use
Other font styles liked:
• CEREBRI, CODE PRO

Colors
0054AA
0677BA
7BADD7
CADEEF
E8F1F8

Requirements
Must have
• CLEAN, NEAT, CLEAR, BUT VERY PROFESSIONAL LOOK
Nice to have
• IMPROVE LAYOUT/GRAPHICS/TABLES/BOXES/DIFFERENT COLOR TEXT IN PLACES, I LIKE PAGES WITH FULL BORDER OR SPLIT PAGE INTO 2 WITH SOME GRAPHIC. ETC.
Should not have
• DONT WANT FANCY. ALL PROFESSIONAL

```html
<!DOCTYPE html>
<html lang="en">
<head>
<meta charset="utf-8">
<title>Bravelton – Physician Booklet Spreads</title>
<link href="https://fonts.googleapis.com/css2?family=Nunito:wght@400;600;700;800&family=Montserrat:wght@400;500&display=swap" rel="stylesheet">
<style>
:root{
  --backdrop:#cdcfd2;
  --navy:#22408c;
  --navy-text:#1f3d8e;
  --sky:#7badd7;
  --ice:#e8eff8;
  --chart-bg:#ebebeb;
  --grid:#c9c9c9;
  --white:#ffffff;
  --ink:#333a48;
  --muted:#b3b8c2;
  --silver:#c8ccd4;
}
*{margin:0;padding:0;box-sizing:border-box}
html,body{width:1200px;height:849px;overflow:hidden;background:var(--backdrop)}
body{position:relative;font-family:"Nunito",sans-serif;color:var(--ink)}
.page{position:absolute;width:220px;height:311px;background:var(--white);overflow:hidden}
.abs{position:absolute}
.body-text{font-size:4.4px;line-height:1.3}
.white{color:var(--white)}
.navy{color:var(--navy-text)}
.h-title{font-weight:800;color:var(--navy-text);line-height:1.1}
.footer-mark{position:absolute;font-size:2.6px;letter-spacing:.2px;color:var(--muted);right:14px;bottom:13px}
.photo{position:absolute}

/* cover */
.cover{background:var(--navy);left:76px;top:82px}
.cover .brand{left:0;width:100%;top:96px;text-align:center;font-family:"Montserrat",sans-serif;font-weight:400;font-size:15px;letter-spacing:1px;color:var(--white)}
.cover .rule{left:60px;width:99px;top:130px;height:1px;background:var(--silver)}
.cover .tagline{left:0;width:100%;top:139px;text-align:center;font-family:"Montserrat",sans-serif;font-size:4.6px;letter-spacing:2.6px;line-height:1.5;color:var(--silver)}
.cover .motto{left:0;width:100%;top:243px;text-align:center;font-family:"Montserrat",sans-serif;font-size:5px;letter-spacing:1.6px;color:var(--white)}

/* founder */
.founder{left:352px;top:82px}
.founder .bio-box{left:75px;top:177px;width:145px;height:73px;background:var(--navy);padding:11px 12px 0 11px;font-size:4.6px;line-height:1.27;color:var(--white);text-align:justify}

/* programs */
.programs{left:628px;top:82px}
.programs .top-band{left:0;top:0;width:100%;height:98px;background:var(--navy)}
.programs .col-left{left:13px;top:14px;width:95px;color:var(--white)}
.programs .col-right{left:112px;top:14px;width:96px;color:var(--white)}
.programs ul{list-style:none}
.programs li{position:relative;padding-left:7px;margin-top:3.6px}
.programs li::before{content:"";position:absolute;left:1px;top:1.6px;width:1.4px;height:1.4px;border-radius:50%;background:var(--white)}
.programs .chart-area{left:0;top:98px;width:100%;height:147px;background:var(--chart-bg)}
.programs .chart-title{left:13px;top:107px;font-size:8.4px;font-weight:800;color:var(--navy-text);letter-spacing:.1px}
.programs .goal{left:13px;top:273px;font-size:8.3px;font-weight:800;color:var(--navy-text)}

/* rpm */
.rpm{left:904px;top:82px}
.rpm .panel{left:57px;top:0;width:163px;height:100%;background:var(--navy)}
.rpm .title{left:79px;top:174px;font-size:10.5px;font-weight:800;color:var(--white);line-height:1.2}
.rpm .dash{left:79px;top:205px;width:22px;height:1.6px;background:var(--white)}
.rpm .copy{left:79px;top:216px;width:118px;color:var(--white)}
.rpm .copy p+p{margin-top:4px}

/* ccm */
.ccm{left:76px;top:456px}
.ccm .band{left:0;top:106px;width:100%;height:46px;background:var(--navy)}
.ccm .title{left:83px;top:72px;font-size:10.3px}
.ccm .band-text{left:83px;top:118px;width:126px;font-size:4.9px;font-weight:700;line-height:1.25;color:var(--white)}
.ccm ul{left:84px;top:172px;width:122px;list-style:none}
.ccm li{position:relative;padding-left:6px;margin-bottom:5px}
.ccm li::before{content:"";position:absolute;left:0;top:1.6px;width:1.4px;height:1.4px;border-radius:50%;background:var(--ink)}

/* why */
.why{left:352px;top:456px}
.why .title{left:13px;top:24px;font-size:13px}
.why .subtitle{left:13px;top:53px;font-family:"Montserrat",sans-serif;font-size:8px;letter-spacing:1.3px;color:var(--ink)}
.why .block-navy{left:0;top:76px;width:112px;height:118px;background:var(--navy)}
.why .block-ice{left:112px;top:76px;width:108px;height:118px;background:var(--ice)}
.why .col{top:84px;text-align:justify}
.why .col p+p{margin-top:8px}
.why .col-left{left:13px;width:93px;color:var(--white)}
.why .col-right{left:116px;width:94px;color:#4a62a8}
.why .col-right b{color:var(--navy-text)}

/* costs */
.costs{left:628px;top:456px;background:var(--ice)}
.costs .band{left:0;top:0;width:100%;height:82px;background:var(--navy)}
.costs .title{left:13px;top:25px;font-size:12.4px;color:var(--white)}
.costs .intro{left:13px;top:53px;width:195px;color:var(--white);text-align:justify;font-size:4.1px}
.costs .h2{left:13px;font-size:9px}
.costs .dash{left:13px;top:120px;width:22px;height:1.6px;background:var(--navy)}
.costs .line{left:13px;font-size:5px;color:var(--ink)}
.costs .paid{left:13px;top:259px;font-size:6.4px;line-height:1.2}

/* patients */
.patients{left:904px;top:451px}
.patients .strip{left:0;top:0;width:48px;height:100%;background:var(--navy)}
.patients .title{left:88px;top:40px;font-size:12.4px}
.patients .name{left:88px;font-size:6.4px;font-weight:800;color:var(--navy-text);width:118px;border-bottom:.6px solid var(--ink);padding-bottom:1px}
.patients .role{left:88px;font-size:4.2px}
.patients .desc{left:88px;width:118px;font-size:3.2px;line-height:1.25;text-align:justify}
</style>
</head>
<body>

<!-- Page 1: cover -->
<section class="page cover">
  <div class="abs brand">BRAVELTON</div>
  <div class="abs rule"></div>
  <div class="abs tagline">CHRONIC CARE<br>EXPERTS</div>
  <div class="abs motto">SAVING LIVES 24/7</div>
</section>

<!-- Page 2: founder -->
<section class="page founder">
  <div class="photo" role="img" aria-label="Founder with his family on a sandy beach" style="left:0;top:0;width:163px;height:196px;background:linear-gradient(180deg,#c9c2ae 0%,#a9b7c7 45%,#8aa5c4 100%)"></div>
  <div class="abs bio-box">Daniel Harwood, RN, BSN started Bravelton One, LLC in 2022 to provide Chronic Care Services with the mission to help people stay at home and out of the hospital. His first job was an orderly in the hospital at age 17. In the past 35 years, he has successfully started, grown, and sold a Physical Therapy clinic, a Home Medical Equipment company, and a Sleep Lab. From 2015 to 2022, he worked as a Critical Care Travel Nurse in 5 states.</div>
</section>

<!-- Page 3: programs and chart -->
<section class="page programs">
  <div class="abs top-band"></div>
  <div class="abs col-left body-text">
    <p>CMS created Chronic Care Management (CCM) in 2015 to improve quality of healthcare and reduce hospital visits which lowers overall healthcare related costs. Statistics show up to 50% cost reduction in patients enrolled in CCM.</p>
    <p style="margin-top:8px;font-weight:800">What makes your patients Eligible?</p>
    <p style="margin-top:2px">Medicare Part B or a Medicare Advantage Plan/ Supplemental Plan with two or more Chronic Conditions.</p>
  </div>
  <div class="abs col-right body-text">
    <p style="font-weight:800">Our Programs (Enrollment % of your total Medicare Population)</p>
    <ul>
      <li style="font-weight:800">Chronic Care Management</li>
      <li>2 Chronic Conditions <b>(80% Enrollment)</b></li>
      <li style="font-weight:800">Remote Patient Monitoring (RPM)</li>
      <li>BP, Pulse Ox, Glucometer, Scale <b>(70% Enrollment)</b></li>
      <li style="font-weight:800">Behavioral Health (BHI)</li>
      <li>1 Mental Health condition <b>(60% Enrollment)</b></li>
    </ul>
  </div>
  <div class="abs chart-area"></div>
  <div class="abs chart-title">CHRONIC CONDITION PREVALENCE &gt; 65 YRS</div>
  <svg class="abs" style="left:0;top:118px" width="220" height="125" viewBox="0 0 220 125" font-family="Nunito, sans-serif" font-size="3.4" fill="#555">
    <g stroke="#c9c9c9" stroke-width=".4">
      <line x1="95.7" y1="3" x2="95.7" y2="115"/>
      <line x1="140.3" y1="3" x2="140.3" y2="115"/>
      <line x1="185" y1="3" x2="185" y2="115"/>
    </g>
    <g text-anchor="end">
      <text x="49" y="8.5">HTN</text><text x="49" y="20">HLD</text><text x="49" y="31.5">CKD</text>
      <text x="49" y="43">OBESITY</text><text x="49" y="54.5">MEMORY</text><text x="49" y="66">DIABETES</text>
      <text x="49" y="77.5">PAIN</text><text x="49" y="89">CANCER</text><text x="49" y="100.5">COPD</text><text x="49" y="112">CHF</text>
    </g>
    <g fill="#22408c">
      <rect x="51" y="5" width="128.6" height="3.2"/><rect x="51" y="16.5" width="89.3" height="3.2"/>
      <rect x="51" y="28" width="76.8" height="3.2"/><rect x="51" y="39.5" width="76.8" height="3.2"/>
      <rect x="51" y="51" width="76.8" height="3.2"/><rect x="51" y="62.5" width="58.9" height="3.2"/>
      <rect x="51" y="74" width="58.9" height="3.2"/><rect x="51" y="85.5" width="44.7" height="3.2"/>
      <rect x="51" y="97" width="39.3" height="3.2"/><rect x="51" y="108.5" width="39.3" height="3.2"/>
    </g>
    <g text-anchor="middle">
      <text x="51" y="121.5">0%</text><text x="95.7" y="121.5">25%</text><text x="140.3" y="121.5">50%</text><text x="185" y="121.5">75%</text>
    </g>
  </svg>
  <div class="abs body-text" style="left:13px;top:252px;width:165px;font-size:4px;font-weight:700">Bravelton maximizes access to all available resources, minimizes barriers to compliance, and encourages positive lifestyle choices. Our nurses are personal advocates for your clients.</div>
  <div class="abs goal">Our # 1 Goal is to prevent MIs and CVAs.</div>
  <div class="footer-mark">BRAVELTON | CHRONIC CARE EXPERTS</div>
</section>

<!-- Page 4: RPM -->
<section class="page rpm">
  <div class="abs panel"></div>
  <div class="photo" role="img" aria-label="Remote monitoring devices: blood pressure cuff and monitor, pulse oximeter, glucometer and bathroom scale" style="left:26px;top:31px;width:194px;height:125px;border-radius:6px;background:linear-gradient(135deg,#e4e6ea 0%,#f4f5f7 45%,#b9bec8 100%)"></div>
  <div class="abs title">RPM- Remote Patient<br>Monitoring</div>
  <div class="abs dash"></div>
  <div class="abs copy body-text">
    <p>Remote monitoring devices are provided which track blood pressure, weight, oxygen, glucose and automatically upload to our software sending us alerts in real time. Alerts are monitored and addressed 24/7.</p>
    <p>RN's provide critical thinking and assessments for patients around the clock. If intervention is needed we notify provider with data for new meds, sick visit, or referral to urgent/emergent care. Notifications to providers and staff are sent as telephone encounters via ChartLink for seamless communication from nurses to provider.</p>
  </div>
</section>

<!-- Page 5: CCM / BHI -->
<section class="page ccm">
  <div class="abs band"></div>
  <div class="photo" role="img" aria-label="Hand holding a desk telephone handset" style="left:9px;top:66px;width:70px;height:61px;border-radius:0 0 0 6px;background:linear-gradient(135deg,#d9d9db 0%,#6f7278 55%,#2c2f35 100%)"></div>
  <div class="abs h-title title">CCM- Chronic Care<br>BHI-Behavioral Health</div>
  <div class="abs band-text">A Registered Nurse will be accessible by phone 24 / 7 for addressing patient needs such as assessments, refills, education, and expediting sick visits.</div>
  <ul class="abs body-text">
    <li>Assisting in referrals to specialists and home care services.</li>
    <li>Assisting with social services, transportation, and medical equipment and supplies.</li>
    <li>Scheduling any preventive care needed.</li>
    <li>Providing nutritional education and supporting positive lifestyle changes.</li>
  </ul>
  <div class="footer-mark">BRAVELTON | CHRONIC CARE EXPERTS</div>
</section>

<!-- Page 6: Why -->
<section class="page why">
  <div class="abs h-title title">Why Bravelton?</div>
  <div class="abs subtitle">WE STAFF LOCAL RN’S</div>
  <div class="abs block-navy"></div>
  <div class="abs block-ice"></div>
  <div class="abs col col-left body-text">
    <p>Bravelton guarantees a dedicated team of <b>Critical Care RN’s, LPN’s and Medical Assistants.</b> We continue to build our team with the most <b>experienced and passionate</b> advocates to ensure the absolute best service for your clients.</p>
    <p>Bravelton bridges the gap between clinical and home environments. We prioritize <b>following up</b> and following through which results in better coordination of care and the best possible outcomes.</p>
    <p>We maintain 100% compliance with <b>Annual Wellness Visits.</b> Maintaining the <b>highest standards</b> is a priority for our team and is what sets us apart from other Chronic Care Providers.</p>
  </div>
  <div class="abs col col-right body-text">
    <p>Using ChartLink guarantees seamless integration into your practice. The GOAL is for clients to call CCM 24/7 phone instead of main office for all needs. <b>This eliminates non-billable staff time.</b></p>
    <p>Our <b>average monthly reimbursement is $125 greater than the national average</b> because we believe in spending as much time with our patients as needed.</p>
    <p>Our daily average is <b>70 outgoing calls and 40 incoming calls.</b> We typically respond to <b>65</b> RPM alerts and <b>10</b> Telephone Encounters daily. We send several patients to ER weekly.</p>
  </div>
  <div class="footer-mark">BRAVELTON | CHRONIC CARE EXPERTS</div>
</section>

<!-- Page 7: Start up costs -->
<section class="page costs">
  <div class="abs band"></div>
  <div class="abs h-title title">Start Up Costs</div>
  <div class="abs intro body-text">Bravelton covers all upfront costs including ChartLink, clinical and billing staff, providers’ staff orientation, and all marketing materials (mass email, magnetic business cards with 24/7 phone number, brochures, posters, and webpage for your current website). RPM devices will cost over $100,00</div>
  <div class="abs h-title h2" style="top:98px">Monthly Net Profit per 1000 clients</div>
  <div class="abs dash"></div>
  <div class="abs h-title h2" style="top:135px">Building Phase</div>
  <div class="abs line" style="top:150px">First 6 months $50,000 ($50 per patient)</div>
  <div class="abs h-title h2" style="top:173px">Management Phase</div>
  <div class="abs line" style="top:188px">After 6 months $100,000 ($100 per patient)</div>
  <div class="abs h-title paid">Bravelton gets paid after<br>Medicare pays you!</div>
  <div class="photo" role="img" aria-label="Silver three-dimensional dollar sign" style="left:156px;top:231px;width:52px;height:66px;border-radius:8px;background:linear-gradient(135deg,#f2f3f5 0%,#b8bcc4 55%,#e3e6ea 100%)"></div>
</section>

<!-- Page 8: Happy patients -->
<section class="page patients">
  <div class="abs strip"></div>
  <div class="abs h-title title">Happy<br>Patients...</div>

  <div class="photo" role="img" aria-label="Black and white portrait of a smiling man in a suit" style="left:17px;top:69px;width:62px;height:65px;background:linear-gradient(180deg,#e6e6e6 0%,#8d8d8d 60%,#3a3a3a 100%)"></div>
  <div class="abs name" style="top:94px">Arif Santoso</div>
  <div class="abs role" style="top:106px">Product Designer</div>
  <div class="abs desc" style="top:119px">Booklets are printed materials with four or more pages, containing details about a business, event, product, promotion, etc. They are also known as catalogs or pamphlets, and are usually created to communicate a message to a wide variety of audiences.</div>

  <div class="photo" role="img" aria-label="Black and white portrait of a smiling bearded man in a suit" style="left:17px;top:138px;width:62px;height:65px;background:linear-gradient(180deg,#e9e9e9 0%,#909090 60%,#3d3d3d 100%)"></div>
  <div class="abs name" style="top:161px">Emeka Obi</div>
  <div class="abs role" style="top:173px">Marketer</div>
  <div class="abs desc" style="top:188px">Booklets are printed materials with four or more pages, containing details about a business, event, product, promotion, etc. They are also known as catalogs or pamphlets, and are usually created to communicate a message to a wide variety of audiences.</div>

  <div class="photo" role="img" aria-label="Black and white portrait of a woman wearing glasses" style="left:17px;top:207px;width:62px;height:64px;background:linear-gradient(180deg,#efefef 0%,#9a9a9a 60%,#444 100%)"></div>
  <div class="abs name" style="top:232px">Yumi Tanaka</div>
  <div class="abs role" style="top:244px">Graphic Designer</div>
  <div class="abs desc" style="top:257px">Booklets are printed materials with four or more pages, containing details about a business, event, product, promotion, etc. They are also known as catalogs or pamphlets, and are usually created to communicate a message to a wide variety of audiences.</div>

  <div class="footer-mark">BRAVELTON | CHRONIC CARE EXPERTS</div>
</section>

</body>
</html>
```